Swim school needs flyer design

Need revamp of flyer design. Attached last years flyer (RTC A4 Holiday Leaflet-v6.2 (1)). Also attached is this years information in word format (RTC A4 RTC & Holiday Leaflet 2014-2015).
This flyer must fit with our logo (Ripple Tide Club-RGB). This flyer is our first point of call for many of our clients. With the amount of information that must be provided, it is important that it flows and is appealing. Photos can be accessed from http://marlapics.fotonest.example/apps/photos/album?albumid=27391540 or from your own source
Important that the final design fits printers template.(Flyers-A4-210x297mm-2Side - attached)

```html
<!DOCTYPE html>
<html lang="en">
<head>
<meta charset="utf-8">
<title>Ripple Tide Club – Flyers 2014/15</title>
<link rel="stylesheet" href="https://fonts.googleapis.com/css2?family=Nunito:wght@800;900&family=Roboto+Condensed:wght@400;700&family=Arimo:wght@400;700&display=swap">
<style>
:root{
  --bg:#4a3a30;
  --sky:#1fa9e1;
  --sky-dark:#1384c4;
  --navy:#0e2340;
  --orange:#f39322;
  --orange-dark:#e07b12;
  --lime:#a9c92f;
  --lime-dark:#8fb322;
  --red:#e3202a;
  --charcoal:#3b3b3b;
  --ink:#1f1f1f;
  --paper:#ffffff;
  --water-a:#4ab7d8;
  --water-b:#1b86b4;
}
*{box-sizing:border-box;margin:0;padding:0}
html,body{width:1200px;height:852px;overflow:hidden;background:var(--bg)}
body{position:relative;font-family:"Arimo",Arial,sans-serif;color:var(--ink)}
.flyer{position:absolute;top:70px;width:520px;height:727px;background:var(--paper);overflow:hidden}
.flyer--term{left:80px}
.flyer--holiday{left:619px}
.abs{position:absolute}
.header-wave{position:absolute;left:0;top:0;width:520px;height:140px}
.header-title{left:17px;top:14px;font:700 21px "Roboto Condensed",Arial,sans-serif;color:var(--navy)}
.header-call{font:700 24px "Roboto Condensed",Arial,sans-serif;color:#fff}
.header-url{right:18px;top:12px;font:700 16px "Roboto Condensed",Arial,sans-serif;color:var(--navy)}
.brand{display:flex;align-items:center;gap:7px}
.brand-dot{width:16px;height:16px;border-radius:50%;background:var(--orange)}
.brand-name{font:800 21px "Nunito",Arial,sans-serif;color:var(--sky-dark)}
.main-title{left:0;width:520px;text-align:center;font:900 36px "Nunito",Arial,sans-serif;color:var(--sky);text-shadow:1px 2px 2px rgba(0,0,0,.35);white-space:nowrap}
.main-title--orange{color:var(--orange);font-size:42px}
.section-head{font:700 14px "Arimo",Arial,sans-serif;color:var(--orange)}
.ticks{list-style:none}
.ticks li{position:relative;padding-left:14px;font-size:7.4px;line-height:1.4;margin-bottom:3px;color:var(--ink)}
.ticks li::before{content:"";position:absolute;left:0;top:1px;width:7px;height:7px;border:1px solid #777;background:#fff}
.ticks li::after{content:"";position:absolute;left:2px;top:1px;width:3px;height:5px;border:solid var(--orange-dark);border-width:0 1.5px 1.5px 0;transform:rotate(40deg)}
.pathway{left:384px;top:204px;width:106px;height:158px;background:var(--orange);border:3px solid #fff;border-radius:40px;box-shadow:0 0 0 1px #ddd,0 2px 4px rgba(0,0,0,.25);text-align:center;color:#fff;padding-top:10px}
.pathway h3{font:700 10px/1.15 "Roboto Condensed",Arial,sans-serif;margin-bottom:6px}
.pathway b{display:block;font:700 6.6px "Arimo",Arial,sans-serif;color:var(--navy);margin-top:5px}
.pathway small{display:block;font-size:5px;color:#fff}
.term-card{top:373px;width:115px;height:157px;background:var(--lime);border-radius:6px;padding:5px 6px;color:var(--navy);box-shadow:0 1px 3px rgba(0,0,0,.3)}
.term-card .year{font:700 18px "Roboto Condensed",Arial,sans-serif;color:#fff}
.term-card .term{font:700 11px/1.35 "Roboto Condensed",Arial,sans-serif;color:#111}
.term-card .note{font-size:7px;line-height:1.3;margin:5px 0 8px;color:#333}
.prices{width:100%;border-collapse:collapse;font-size:9px;font-weight:700;color:#111}
.prices td{padding:1.5px 0}
.prices td+td{text-align:left;padding-left:6px}
.band{left:0;width:520px;height:17px;background:var(--red);color:#fff;font-size:6.6px;text-align:center;line-height:17px;white-space:nowrap}
.photo{left:0;width:520px;background:linear-gradient(160deg,var(--water-a),var(--water-b))}
.photo-swoosh{position:absolute;left:0;width:520px}
.foot-note{font:400 9px/2 "Arimo",Arial,sans-serif;color:#fff;text-align:center}
.holiday-box{left:28px;top:200px;width:190px;height:146px;background:var(--orange);border-radius:6px;padding:4px 7px;box-shadow:0 1px 3px rgba(0,0,0,.3)}
.holiday-box h3{font:700 15px "Roboto Condensed",Arial,sans-serif;color:#fff;text-align:center;margin-bottom:3px}
.dates-panel{background:var(--charcoal);border-radius:4px;padding:3px 6px;color:#fff}
.dates-panel .yr{font:700 12px "Roboto Condensed",Arial,sans-serif;color:var(--lime)}
.date-grid{display:grid;grid-template-columns:1fr 1fr;gap:1px 4px;font-size:8.5px;margin:2px 0 3px}
.date-grid span::before{content:"\2611";color:#fff;margin-right:3px;font-size:9px}
.price-pill{margin:5px auto 0;width:160px;background:var(--sky);border-radius:8px;font-size:6.5px;color:#fff;text-align:center;padding:1px 0}
.pools{left:255px;top:200px;width:236px;height:216px;background:var(--lime);border-radius:6px;padding:6px 5px;box-shadow:0 1px 3px rgba(0,0,0,.3)}
.pools h3{font:700 13px/1.25 "Roboto Condensed",Arial,sans-serif;color:#fff;padding-left:10px;margin-bottom:6px}
.pool-card{background:var(--orange);border-radius:5px;margin-bottom:5px;padding:4px 8px;color:var(--navy);font-size:6px;line-height:1.45}
.pool-card h4{font:700 9.5px "Roboto Condensed",Arial,sans-serif;color:#fff;margin-bottom:4px}
.booking{left:32px;top:360px;width:210px}
.booking strong{display:block;font-size:9px;line-height:1.4}
.booking p{font-size:7px;margin-top:4px}
.salt{right:22px;top:427px;width:240px;text-align:right;font:700 15.5px/1.45 "Roboto Condensed",Arial,sans-serif;color:var(--sky)}
.call-orange{right:28px;top:503px;font:700 26px "Roboto Condensed",Arial,sans-serif;color:var(--orange)}
.address-foot{right:10px;bottom:8px;text-align:right;font:400 8px/1.9 "Arimo",Arial,sans-serif;color:var(--navy)}
</style>
</head>
<body>

<section class="flyer flyer--term">
  <svg class="header-wave" viewBox="0 0 520 140" aria-hidden="true">
    <path d="M0 0H520V70C420 96 300 40 170 92C100 118 40 110 0 112Z" fill="var(--sky)"/>
    <path d="M0 112C60 116 120 104 190 84C300 54 420 76 520 64V74C420 88 300 66 200 94C130 114 60 124 0 120Z" fill="#fff"/>
    <path d="M0 122C70 128 140 112 210 98C320 72 420 90 520 80V84C420 96 320 82 220 104C140 122 70 134 0 130Z" fill="var(--sky)"/>
  </svg>
  <h2 class="abs header-title">2014/15 Term Dates &amp; Prices</h2>
  <div class="abs header-call" style="left:17px;top:47px">Call: 95550142</div>
  <div class="abs brand" style="left:302px;top:86px"><span class="brand-dot"></span><span class="brand-name">Ripple Tide Club</span></div>

  <h1 class="abs main-title" style="top:136px">Ripple Tide Club Classes</h1>

  <h3 class="abs section-head" style="left:22px;top:221px">Important</h3>
  <ul class="abs ticks" style="left:22px;top:245px;width:275px">
    <li>No bookings are taken without a fully completed enrolment form and payment.</li>
    <li>Read RTC Policies and Procedures for information on discounts, payment methods, refunds and makeups.</li>
    <li>Book early – place are limited due to small class sizes.</li>
    <li>Bookings can only be made in person at our Elmsford Office or online.</li>
    <li>During holidays, all bookings must be done via the Elmsford Office.</li>
    <li>Photographs and video footage is not allowed to be taken without the permission of all the parents/ guardians whose children are in the class.</li>
  </ul>

  <aside class="abs pathway">
    <h3>Our Streamlined<br>Pathway to<br>Success</h3>
    <b>BABY AWARENESS</b><small>½ hour class per week</small>
    <b>BABY TRANSITION CLASSES</b><small>½ hour class per week</small>
    <b>RIPPLE TIDE CLUB CLASSES</b><small>½ hour class per week</small>
    <b>TRANSITIONAL STROKE GROUP</b><small>1 hour class per week</small>
  </aside>

  <article class="abs term-card" style="left:20px">
    <div class="year">*2014:</div>
    <div class="term">Term 4-10 week term<br>Oct 6th - Dec 14th</div>
    <p class="note">Bookings taken from 22nd Sep 2014</p>
    <table class="prices"><tr><td>Babies</td><td>$155</td></tr><tr><td>Transition</td><td>$165</td></tr><tr><td>RTC</td><td>$170</td></tr><tr><td>TSG</td><td>$210</td></tr></table>
  </article>
  <article class="abs term-card" style="left:141px">
    <div class="year">*2015:</div>
    <div class="term">Term 1-9 week term<br>Jan 27th - Mar 29th</div>
    <p class="note">Bookings taken from 15th Dec 2014</p>
    <table class="prices"><tr><td>Babies</td><td>$139.50</td></tr><tr><td>Transition</td><td>$148.50</td></tr><tr><td>RTC</td><td>$153</td></tr><tr><td>TSG</td><td>$189</td></tr></table>
  </article>
  <article class="abs term-card" style="left:262px">
    <div class="year">*2015:</div>
    <div class="term">Term 2-11 week term<br>Apr 13th - Jun 28th</div>
    <p class="note">Bookings taken from 30th Mar 2015</p>
    <table class="prices"><tr><td>Babies</td><td>$170.50</td></tr><tr><td>Transition</td><td>$176</td></tr><tr><td>RTC</td><td>$181.50</td></tr><tr><td>TSG</td><td>$231</td></tr></table>
  </article>
  <article class="abs term-card" style="left:384px">
    <div class="year">*2015:</div>
    <div class="term">Term 3-10 week term<br>Jul 13th - Sep 20th</div>
    <p class="note">Bookings taken from 29th Jun 2015</p>
    <table class="prices"><tr><td>Babies</td><td>$160</td></tr><tr><td>Transition</td><td>$170</td></tr><tr><td>RTC</td><td>$175</td></tr><tr><td>TSG</td><td>$215</td></tr></table>
  </article>

  <div class="abs band" style="top:534px">All swimmers, male and female, are required to wear a cap – please name your cap and goggles with a biro to prevent it washing off.</div>
  <div class="abs photo" style="top:551px;height:176px" role="img" aria-label="Photo of young children swimming with a kickboard and an instructor in a pool"></div>
  <svg class="photo-swoosh" style="top:600px;height:127px" viewBox="0 0 520 127" aria-hidden="true">
    <path d="M0 110C120 70 260 20 520 60V30C300 0 150 50 0 95Z" fill="var(--lime)" opacity=".85"/>
    <path d="M0 127V108C150 70 300 40 520 70V127Z" fill="var(--orange)"/>
    <path d="M0 108C150 70 300 40 520 70V76C300 48 150 80 0 116Z" fill="#fff"/>
  </svg>
  <p class="abs foot-note" style="right:14px;bottom:4px;width:210px">* Note that these terms have public holidays<br>and prices will be adjusted accordingly.</p>
</section>

<section class="flyer flyer--holiday">
  <svg class="header-wave" viewBox="0 0 520 140" aria-hidden="true">
    <path d="M0 0H520V110C460 104 400 60 300 70C200 80 120 30 0 50Z" fill="var(--sky)"/>
    <path d="M0 50C120 28 200 76 300 66C400 58 460 98 520 106V114C460 106 400 68 300 76C200 86 120 40 0 58Z" fill="#fff"/>
    <path d="M0 60C120 44 200 90 300 82C400 74 460 112 520 120V124C460 118 400 82 300 88C200 96 120 52 0 66Z" fill="var(--sky)"/>
  </svg>
  <div class="abs header-url">rippletideclub.example.au</div>
  <div class="abs header-call" style="right:18px;top:42px">Call: 95550142</div>
  <div class="abs brand" style="left:30px;top:96px"><span class="brand-dot"></span><span class="brand-name">Ripple Tide Club</span></div>

  <h1 class="abs main-title main-title--orange" style="top:138px">Holiday Swim Classes</h1>

  <div class="abs holiday-box">
    <h3>Holiday Program Dates</h3>
    <div class="dates-panel">
      <div class="yr">2014</div>
      <div class="date-grid"><span>Sep 23rd - 27th</span><span>Sep 30th - Oct 4th</span></div>
    </div>
    <div class="dates-panel" style="margin-top:3px">
      <div class="yr">2015</div>
      <div class="date-grid"><span>Jan 13th - 17th</span><span>Jan 20th - 24th</span><span>Mar 30th - Apr 3rd</span><span>Apr 6th - 10th</span><span>Jun 29th - Jul 3rd</span></div>
    </div>
    <div class="price-pill">* $52 per child due to 4 day week</div>
  </div>

  <aside class="abs pools">
    <h3>Pool Locations Contact<br>Details &amp; Office Hours</h3>
    <div class="pool-card"><h4>ELMSFORD P.S. POOL</h4><b>Location:</b> 27 Wren Street, Elmsford 3091 &nbsp;Phone: 9555 0142<br><b>Office Hours:</b> Mon-Fri 9:00am-5.30pm, Sat-Sun 9.15am-12.15pm</div>
    <div class="pool-card"><h4>CORRAN GRAMMAR POOL</h4><b>Location:</b> Gate 1, Ashby Street, Corran 3097.</div>
    <div class="pool-card"><h4>ALL CORRESPONDENCE</h4><b>Post:</b> P.O. Box 4410, East Corran 3097<br>Email: info@rippletideclub.example.au<br>ABN: 12 345 678 901</div>
  </aside>

  <div class="abs booking">
    <strong>No bookings are taken without a fully completed enrolment form and payment.</strong>
    <p>Places are limited so book early to avoid disappointment.</p>
  </div>

  <h3 class="abs section-head" style="left:32px;top:415px">Important</h3>
  <ul class="abs ticks" style="left:32px;top:440px;width:210px">
    <li>All holiday swim classes are conducted at the Elmsford primary school pool</li>
    <li>30 minute classes run every ½ hour from 9.30am to 12 noon</li>
    <li>Limited places due to small class sizes</li>
    <li>Beginners to advanced swimmers welcome</li>
    <li>All children are grouped by age and ability</li>
    <li>No refunds or makeups for holiday programs</li>
  </ul>

  <p class="abs salt">Salt Water Pool Ages 3 and older<br>$75 per child per week (5x½ hour classes per week)</p>
  <div class="abs call-orange">Call: 95550142</div>

  <div class="abs band" style="top:543px">Our qualified staff makes swimming lessons not only a rewarding but also a lot of fun. This is a great opportunity to kick-start your child's aquatic education.</div>
  <div class="abs photo" style="top:560px;height:167px" role="img" aria-label="Photo of children in swim caps and goggles floating on pool noodles"></div>
  <svg class="photo-swoosh" style="top:600px;height:127px" viewBox="0 0 520 127" aria-hidden="true">
    <path d="M0 127V100C160 80 300 60 520 90V127Z" fill="var(--orange)"/>
    <path d="M0 100C160 80 300 60 520 90V96C300 68 160 88 0 108Z" fill="#fff"/>
    <path d="M0 92C120 70 220 40 330 30C260 50 160 80 0 100Z" fill="var(--lime)" opacity=".85"/>
  </svg>
  <p class="abs address-foot">Elmsford P.S. Pool, 27 Wren Street Elmsford<br>Corran Grammar Pool, Gate 1, Ashby St Corran</p>
</section>

</body>
</html>
```